Brivo Wellness Co Business Card for food and Beverage Wizards & Alchemists

One main business card design for a wellness enterprise which represents two brands. We need one primary card design, for two different employees. The only difference between the cards will be the name, title and phone number for each employee, all other design elements will be same.
I've uploaded the logos for each brand. I have also uploaded a mockup which I made using Google's drawing tool. I can provide example images of business cards we find attractive if you would like some help picturing what we like.
I'm picturing the color splash on the back of the card below the two logos to be a dark burgundy or blue. This may sound a bit silly but the feel of the card and color should look almost like wizard dress robes. Dark emerald green, dark blue and dark burgundy with black undertones and gold lace.

Target Market(s)

Healthy food and beverage industry

Industry/Entity Type

Health And Wellness

Contact Information for Business Card

On one side we would like the business name, location, title of employee, employee name and contact details. On the flip side we would like our two brand logos and a splash of color. We would like the card to have a black font with some gold accents if possible. We would also like the trim of the business card or a middle ply within the card stock to have a color other than white.

Font styles to use
Serif

Colors
ec1f27
0255a3
00a990

Requirements
Must have
• Bold dark colors, happy to provide sample photos of business cards I like from pinterest. Must have a version for two different employees. Must be sharp, modern and chic.
Nice to have
• Thick card stock layer in between the front and back of card that is either black or gold lace or something to make it feel, well let's say to make it feel expensive.
Should not have
• Should not have any cartoon-ey elements. All business.

```html
<!DOCTYPE html>
<html lang="en">
<head>
<meta charset="utf-8">
<title>Brivo Wellness Co Business Card</title>
<link href="https://fonts.googleapis.com/css2?family=Cinzel:wght@400&family=Montserrat:wght@400;700&display=swap" rel="stylesheet">
<style>
  :root {
    --backdrop: #2a2a2b;
    --card: #252526;
    --edge: #4a0f22;
    --white: #f2f2f2;
    --gold: #b89a4e;
  }
  * { box-sizing: border-box; margin: 0; padding: 0; }
  html, body {
    width: 1200px; height: 1017px; overflow: hidden;
    background: var(--backdrop);
  }
  .canvas { position: relative; width: 1200px; height: 1017px; }
  .card {
    position: absolute;
    width: 560px; height: 320px;
    background: var(--card);
    border: 4px solid var(--edge);
    border-radius: 3px;
  }
  .card--back { left: 90px; top: 110px; }
  .card--front { left: 550px; top: 580px; }

  .brand {
    position: absolute; top: 0; bottom: 0; width: 50%;
    display: flex; flex-direction: column; align-items: center; justify-content: center;
  }
  .brand--left { left: 0; }
  .brand--right { right: 0; }
  .brand__mark {
    display: flex; align-items: center; gap: 10px;
    font-family: "Cinzel", serif; font-weight: 400;
    font-size: 24px; color: var(--white); letter-spacing: 1px;
    height: 120px;
  }
  .brand__dot { width: 12px; height: 12px; border-radius: 50%; background: var(--white); }
  .brand__url {
    margin-top: 18px;
    font-family: "Montserrat", sans-serif; font-size: 12px;
    letter-spacing: 4px; color: var(--white); text-transform: uppercase;
  }

  .contact {
    position: absolute; inset: 0;
    display: flex; flex-direction: column; align-items: center; justify-content: center;
    color: var(--gold); text-align: center;
  }
  .contact__name { font-family: "Cinzel", serif; font-size: 26px; letter-spacing: 1px; line-height: 1.1; }
  .contact__title { font-family: "Montserrat", sans-serif; font-size: 13px; letter-spacing: 1px; text-transform: uppercase; margin-bottom: 14px; }
  .contact__company { font-family: "Montserrat", sans-serif; font-weight: 700; font-size: 12px; text-transform: uppercase; }
  .contact__place { font-family: "Montserrat", sans-serif; font-size: 12px; text-transform: uppercase; margin-bottom: 14px; }
  .contact__line { font-family: "Montserrat", sans-serif; font-size: 12px; text-transform: uppercase; line-height: 1.5; }
</style>
</head>
<body>
<main class="canvas">
  <section class="card card--back" aria-label="Card back with brand names">
    <div class="brand brand--left">
      <div class="brand__mark"><span class="brand__dot"></span>Orion Vessel</div>
      <p class="brand__url">orionvessel.com</p>
    </div>
    <div class="brand brand--right">
      <div class="brand__mark">Trine Bevs</div>
      <p class="brand__url">trinebevs.com</p>
    </div>
  </section>

  <section class="card card--front" aria-label="Card front with contact details">
    <div class="contact">
      <h1 class="contact__name">Elias Marlow</h1>
      <p class="contact__title">Beverage Alchemist</p>
      <p class="contact__company">Brivo Wellness Co</p>
      <p class="contact__place">Calloway, CA</p>
      <p class="contact__line">415.555.0192</p>
      <p class="contact__line">brivowellnessco@mail.com</p>
    </div>
  </section>
</main>
</body>
</html>
```